Business Card Design

Our Motto is "Protecting Australia's Underground Utilities"

We want the Southern Cross inside a shield I have attached the southern cross and our old shield design

Product description is: Vacuum Excavation & Utility Location
Wet & Dry Vacuum Loading
Confined Space Entry Specialists
High Pressure Cleaning

The Southern Cross in the shield must be blue and white. The Company name must be Coastal Pipeline Guard. The Green & Gold Shield logo I uploaded is my OLD logo design. Thank you

Target Market(s)

Civil Construction

Industry/Entity Type

Business

Contact Information for Business Card

Coastal Pipeline Guard Pty Ltd
Corey Hallworth(Director)
0413862051
coreyh@pipeguardco.com.au
A.B.N.52938407716

Colors
0456a3

Requirements
Must have
• Southern Cross inside a shield, Blue and white design on the Southern Cross shield.
Must say Coastal Pipeline Guard P/L

```html
<!DOCTYPE html>
<html lang="en">
<head>
<meta charset="utf-8">
<title>Coastal Pipeline Guard – Business Card</title>
<link href="https://fonts.googleapis.com/css2?family=Arimo:wght@400;700&family=Open+Sans:ital,wght@0,400;0,600;1,400&display=swap" rel="stylesheet">
<style>
  :root {
    --stage: #e9ebef;
    --navy-deep: #0a2a66;
    --navy: #0b3a86;
    --brand-blue: #0456a3;
    --glow-blue: #1767c0;
    --ink-blue: #1a5bb0;
    --paper: #ffffff;
    --text-light: #e6eefb;
  }
  * { box-sizing: border-box; margin: 0; padding: 0; }
  html, body {
    width: 1200px; height: 675px; overflow: hidden;
    background: var(--stage);
  }
  .stage {
    position: relative; width: 1200px; height: 675px;
  }
  .card {
    position: absolute; top: 188px;
    width: 520px; height: 298px;
    border-radius: 3px;
    overflow: hidden;
    box-shadow: 0 6px 18px rgba(10, 30, 70, 0.18);
  }

  /* Front */
  .card--front {
    left: 50px;
    background: radial-gradient(ellipse 70% 80% at 45% 28%, var(--glow-blue) 0%, var(--navy) 50%, var(--navy-deep) 100%);
    color: var(--paper);
    text-align: center;
    font-family: "Open Sans", sans-serif;
  }
  .brand {
    display: flex; flex-direction: column; align-items: center;
    gap: 8px;
  }
  .card--front .brand { margin-top: 40px; }
  .brand__dot {
    width: 38px; height: 38px; border-radius: 50%;
    background: var(--paper);
  }
  .brand__name {
    font-family: "Arimo", sans-serif;
    font-weight: 700; font-size: 11px; color: var(--paper);
    letter-spacing: 0.2px;
  }
  .motto {
    margin-top: 26px;
    font-size: 17px; font-weight: 400; letter-spacing: 0.3px;
  }
  .services {
    margin-top: 12px;
    font-size: 11px; line-height: 1.6; color: var(--text-light);
  }

  /* Back */
  .card--back { left: 630px; background: var(--paper); }
  .card--back .wave { position: absolute; inset: 0; }
  .card--back .brand {
    position: absolute; top: 24px; left: 148px;
  }
  .contacts {
    position: absolute; left: 26px; top: 156px;
    list-style: none;
    font-family: "Arimo", sans-serif; font-size: 12px;
    color: var(--ink-blue); line-height: 1.45;
  }
  .contacts li { display: flex; align-items: center; gap: 6px; }
  .contacts svg { width: 11px; height: 11px; fill: var(--ink-blue); flex: none; }
  .person {
    position: absolute; right: 26px; bottom: 22px; text-align: right;
    font-family: "Arimo", sans-serif; color: var(--ink-blue);
  }
  .person__name { font-size: 17px; font-weight: 700; }
  .person__role { font-size: 12px; margin-top: 2px; }
</style>
</head>
<body>
<main class="stage">

  <section class="card card--front" aria-label="Business card front">
    <div class="brand">
      <span class="brand__dot"></span>
      <span class="brand__name">Coastal Pipeline Guard</span>
    </div>
    <p class="motto">Protecting Australia's Underground Utilities</p>
    <p class="services">
      Vacuum Excavation &amp; Utility Location | Wet &amp; Dry Vacuum Loading<br>
      Confined Space Entry Specialists | High Pressure Cleaning
    </p>
  </section>

  <section class="card card--back" aria-label="Business card back">
    <svg class="wave" viewBox="0 0 520 298" preserveAspectRatio="none" aria-hidden="true">
      <defs>
        <radialGradient id="backGlow" cx="0.55" cy="0.35" r="0.75">
          <stop offset="0" stop-color="#1767c0"/>
          <stop offset="0.55" stop-color="#0b3a86"/>
          <stop offset="1" stop-color="#0a2a66"/>
        </radialGradient>
      </defs>
      <path d="M0,0 H520 V192 C450,208 390,204 330,176 C260,142 150,80 0,72 Z" fill="url(#backGlow)"/>
      <path d="M0,86 C150,94 250,150 320,186 C380,214 450,218 520,204" fill="none" stroke="#0456a3" stroke-width="4"/>
    </svg>

    <div class="brand">
      <span class="brand__dot"></span>
      <span class="brand__name">Coastal Pipeline Guard</span>
    </div>

    <ul class="contacts">
      <li>
        <svg viewBox="0 0 24 24"><path d="M6.6 10.8a15 15 0 0 0 6.6 6.6l2.2-2.2a1 1 0 0 1 1-.25 11.4 11.4 0 0 0 3.6.6 1 1 0 0 1 1 1V20a1 1 0 0 1-1 1A17 17 0 0 1 3 4a1 1 0 0 1 1-1h3.5a1 1 0 0 1 1 1c0 1.25.2 2.45.6 3.6a1 1 0 0 1-.25 1z"/></svg>
        0413862051
      </li>
      <li>
        <svg viewBox="0 0 24 24"><path d="M2 5h20v14H2z M4 7v.5l8 5 8-5V7z" fill-rule="evenodd"/></svg>
        coreyh@pipeguardco.com.au
      </li>
      <li>
        <svg viewBox="0 0 24 24"><path d="M3 4h18v12H3zM5 6v8h14V6zM8 18h8v2H8z" fill-rule="evenodd"/></svg>
        www.pipeguardco.com.au
      </li>
      <li class="abn">A.B.N.52938407716</li>
    </ul>

    <div class="person">
      <p class="person__name">Corey Hallworth</p>
      <p class="person__role">Director</p>
    </div>
  </section>

</main>
</body>
</html>
```